label design for oral care product

Kindly invite you to design bottle label (114 mm*40 mm) for our product, a kind of oral care product. The GEL is different from our previous cleanser product, as the pic we uploaded for demonstration. The color of frosted glass bottle is dark green, but the cap is white. You could download the pic of bottle among the uploaded files. The logo file and label content description are attached too. Please check them. Our product is made from many kinds of natural plant extracts, which includes herb and fruit. I wish the label would make our product look high-end and reliable. And it would be better if you could give some advice on paper material and special requirements for printing, related to your design. I value the texture of label too, because I think that stands for the quality of products. No color limitation for the use of our logo.
20-40 female, who value oral health.

```html
<!DOCTYPE html>
<html lang="en">
<head>
<meta charset="utf-8">
<title>Lumi Dew Aligner Gel – Label</title>
<link rel="stylesheet" href="https://fonts.googleapis.com/css2?family=Open+Sans:ital,wght@0,400;0,600;0,700;0,800;1,700&display=swap">
<style>
  :root {
    --navy: #2b2d72;
    --navy-deep: #23245e;
    --red: #e3232b;
    --blue-top: #2f4f9b;
    --blue-bottom: #3566b0;
    --white: #ffffff;
    --tag-grey: #e4e6ec;
    --tag-text: #26306e;
    --page: #ffffff;
  }
  * { box-sizing: border-box; margin: 0; padding: 0; }
  html, body {
    width: 1200px; height: 882px; overflow: hidden;
    background: var(--page);
    font-family: "Open Sans", Arial, sans-serif;
  }
  .label {
    position: absolute; left: 105px; top: 268px;
    width: 990px; height: 346px;
    border-radius: 22px; overflow: hidden;
    display: flex;
    box-shadow: 0 10px 30px rgba(0,0,0,0.12);
  }
  .front-panel {
    position: relative; width: 372px; height: 100%;
    background: var(--navy); color: var(--white);
  }
  .front-panel .swoosh { position: absolute; inset: 0; }
  .front-content {
    position: relative; height: 100%;
    display: flex; flex-direction: column; align-items: center;
    text-align: center; padding-top: 48px;
  }
  .brand {
    display: flex; align-items: center; gap: 10px;
    font-weight: 800; font-size: 40px; line-height: 1; letter-spacing: -0.5px;
    color: var(--white);
  }
  .brand-dot { width: 16px; height: 16px; border-radius: 50%; background: var(--white); }
  .product-name {
    margin-top: 44px; font-weight: 700; font-style: italic;
    font-size: 23px; letter-spacing: 0.5px;
  }
  .tagline { margin-top: 14px; font-size: 18.5px; line-height: 1.4; }
  .volume { margin-top: 34px; font-size: 19px; font-weight: 600; }
  .claim-band {
    width: 42px; height: 100%; background: var(--red);
    display: flex; align-items: center; justify-content: center;
  }
  .claim-band span {
    writing-mode: vertical-rl; transform: rotate(180deg);
    color: var(--white); font-size: 17px; white-space: nowrap;
  }
  .info-panel {
    position: relative; flex: 1;
    background: linear-gradient(160deg, var(--blue-top), var(--blue-bottom));
    color: var(--white); padding: 26px 42px 0 28px;
  }
  .info-panel h2 { font-size: 20px; font-weight: 700; margin-bottom: 6px; }
  .info-panel p { font-size: 18.5px; line-height: 1.45; }
  .info-panel .directions { margin-top: 18px; }
  .origin-tag {
    position: absolute; right: 0; bottom: 24px;
    width: 240px; height: 40px;
    background: var(--tag-grey);
    clip-path: polygon(22px 0, 100% 0, 100% 100%, 0 100%);
    display: flex; align-items: center; justify-content: center;
    padding-left: 10px;
    color: var(--tag-text); font-weight: 700; font-style: italic; font-size: 18px;
  }
</style>
</head>
<body>
  <div class="label">
    <section class="front-panel">
      <svg class="swoosh" viewBox="0 0 372 346" preserveAspectRatio="none" aria-hidden="true">
        <path d="M0 178 C 110 150, 240 118, 372 70 L 372 238 C 250 262, 120 272, 0 300 Z" fill="var(--red)"/>
        <path d="M0 300 C 120 272, 250 262, 372 238 L 372 346 L 0 346 Z" fill="var(--navy-deep)"/>
      </svg>
      <div class="front-content">
        <div class="brand"><span class="brand-dot"></span>Lumi Dew</div>
        <h1 class="product-name">ALIGNER GEL</h1>
        <p class="tagline">The Solution to Maintain Dental<br>Hygiene and Strengthen Gums</p>
        <p class="volume">30 ml / 1 fl oz</p>
      </div>
    </section>
    <div class="claim-band"><span>Immune Support for Oral Health</span></div>
    <section class="info-panel">
      <h2>Contains:</h2>
      <p>a proprietary blend of natural plant extract including Angelica, Radix Rehmanniae, Coptis, Honeysuckle, Echinacea, Sage, Chamomile, Acerola cherry.</p>
      <h2 class="directions">Directions:</h2>
      <p>Drop on the teeth directly after brushing. Or, put into clear aligners before wearing again. No need to rinse your mouth with water.</p>
      <div class="origin-tag">Made in Taiwan</div>
    </section>
  </div>
</body>
</html>
```